Private practice for psychiatry and psychotherapy needs a business card and logo

I need a logo and business card design for my private practice for psychiatry and psychotherapy. The optional names for my practice are: Voskuilen Praktijk voor Psychiatrie en Psychotherapie, or short: Praktijk Voskuilen.
I am a (child and adolescent) psychiatrist and psychotherapist. I diagnose and treat infants, children, adolescents and adults with psychiatric symptoms/disorders. I also give supervision to colleagues about their own treatments. My work is characterised by personal involvement, transparence, creativity and professionality.
I would like to have an appealing, light and bright, yet basic design that invites people (both children and adults) to contact me, gives trust and hope, without loosing professional appearance.
I uploaded my contact information which should not necessarily be all included (in this form) on the card as long as people know how to contact me. Please feel free to be creative!
Please note that my website is only temporarely and need a new design and update too!

Target Market(s)

Clients and patients (children, adolescents, adults) with psychiatric symptoms who need diagnosis and treatment. I work with private clients and patients through medical insurances.

Industry/Entity Type

Mental Health

Contact Information for Business Card

Dr. Femke Voskuilen-ter Horst
Psychiater/Kinder- en Jeugdpsychiater
Gerrit Wassinkstraat 4
3063 TW Rotterdam
t: 06-58190274
e: info@praktijkvoskuilen-voorbeeld.nl
i: www.praktijkvoskuilen-voorbeeld.nl

Logo Text

Praktijk Voskuilen voor Psychiatrie en Psychotherapie; or short: Praktijk Voskuilen

Font styles to use
Sans Serif
Other font styles liked:
• up to designer

Requirements
Must have
• Appealing, light, bright, creative, trustful, professional and unique.

```html
<!DOCTYPE html>
<html lang="nl">
<head>
<meta charset="utf-8">
<title>Praktijk Voskuilen – visitekaartje</title>
<link href="https://fonts.googleapis.com/css2?family=Questrial&display=swap" rel="stylesheet">
<style>
  :root {
    --backdrop: #e9e7e4;
    --card-white: #ffffff;
    --brand-orange: #f27b4e;
    --brand-teal: #2bb3a7;
    --ink: #4a4548;
    --rule: #6b6669;
    --white: #ffffff;
    --font: "Questrial", "Century Gothic", sans-serif;
  }
  * { box-sizing: border-box; margin: 0; padding: 0; }
  html, body {
    width: 1200px; height: 852px; overflow: hidden;
    background: var(--backdrop);
    font-family: var(--font);
  }
  .stage {
    position: relative; width: 1200px; height: 852px;
    display: flex; align-items: center; justify-content: center; gap: 48px;
  }
  .card {
    width: 530px; height: 340px; position: relative;
    box-shadow: 0 10px 30px rgba(0,0,0,.18);
  }
  /* front */
  .card--front { background: var(--card-white); }
  .brand {
    position: absolute; left: 60px; top: 128px;
    display: flex; align-items: center; gap: 22px;
  }
  .brand__mark {
    width: 76px; height: 76px; border-radius: 50%;
    background: var(--brand-teal);
  }
  .brand__name {
    font-size: 37px; color: var(--ink); letter-spacing: .5px; line-height: 1;
  }
  .brand__tagline {
    display: flex; align-items: center; gap: 8px; margin-top: 8px;
    font-size: 14px; color: var(--brand-teal); white-space: nowrap;
  }
  .brand__tagline::before, .brand__tagline::after {
    content: ""; flex: 1; height: 1px; background: var(--rule); min-width: 18px;
  }
  /* back */
  .card--back { background: var(--brand-orange); color: var(--white); }
  .back__emblem {
    position: absolute; left: 44px; top: 100px;
    width: 150px; height: 150px; border-radius: 50%;
    background: var(--white);
  }
  .back__divider {
    position: absolute; left: 226px; top: 86px; width: 1px; height: 170px;
    background: rgba(255,255,255,.55);
  }
  .contact {
    position: absolute; left: 246px; top: 84px; right: 16px;
    font-size: 12.5px; line-height: 1.45;
  }
  .contact__name { font-size: 15.5px; letter-spacing: .2px; }
  .contact__role { margin-bottom: 12px; }
  .contact__address { margin-bottom: 10px; }
  .contact__list { list-style: none; }
  .contact__item { display: flex; align-items: center; gap: 8px; }
  .contact__icon { width: 13px; height: 13px; flex: none; }
</style>
</head>
<body>
<main class="stage">
  <section class="card card--front" aria-label="Voorkant visitekaartje">
    <div class="brand">
      <span class="brand__mark" aria-hidden="true"></span>
      <div class="brand__text">
        <div class="brand__name">Praktijk Voskuilen</div>
        <div class="brand__tagline">Voor Psychiatrie en Psychotherapie</div>
      </div>
    </div>
  </section>

  <section class="card card--back" aria-label="Achterkant visitekaartje">
    <span class="back__emblem" aria-hidden="true"></span>
    <span class="back__divider" aria-hidden="true"></span>
    <div class="contact">
      <p class="contact__name">Dr. Femke Voskuilen-ter Horst</p>
      <p class="contact__role">Psychiater/Kinder- en Jeugdpsychiater</p>
      <p class="contact__address">Gerrit Wassinkstraat 4<br>3063 TW Rotterdam</p>
      <ul class="contact__list">
        <li class="contact__item">
          <svg class="contact__icon" viewBox="0 0 16 16" aria-hidden="true"><rect width="16" height="16" rx="3" fill="#fff"/><path d="M5 3.5l2 2-1.2 1.4a6 6 0 003.3 3.3L10.5 9l2 2-1.3 1.5C7.5 12.3 3.7 8.5 3.5 4.8z" fill="#f27b4e"/></svg>
          06-58190274
        </li>
        <li class="contact__item">
          <svg class="contact__icon" viewBox="0 0 16 16" aria-hidden="true"><rect width="16" height="16" rx="3" fill="#fff"/><rect x="3" y="4.5" width="10" height="7" fill="none" stroke="#f27b4e" stroke-width="1.3"/><path d="M3 4.5l5 4 5-4" fill="none" stroke="#f27b4e" stroke-width="1.3"/></svg>
          info@praktijkvoskuilen-voorbeeld.nl
        </li>
        <li class="contact__item">
          <svg class="contact__icon" viewBox="0 0 16 16" aria-hidden="true"><rect width="16" height="16" rx="3" fill="#fff"/><circle cx="8" cy="8" r="4.6" fill="none" stroke="#f27b4e" stroke-width="1.2"/><path d="M3.4 8h9.2M8 3.4c-2.4 2.6-2.4 6.6 0 9.2M8 3.4c2.4 2.6 2.4 6.6 0 9.2" fill="none" stroke="#f27b4e" stroke-width="1"/></svg>
          www.praktijkvoskuilen-voorbeeld.nl
        </li>
      </ul>
    </div>
  </section>
</main>
</body>
</html>
```